information security company tri-fold brochure

Attached is our existing tri-fold PDF and our new logo. We need something that uses the new logo and appropriate color. The wording we will change up a bit, but the existing brochure gives you an idea what it will be like. our customers are banks, finance companies and health care entities so the design should have those sorts of folks in mind.

Security

```html
<!DOCTYPE html>
<html lang="en">
<head>
<meta charset="utf-8">
<title>Corvane Group – Tri-fold Brochure</title>
<link href="https://fonts.googleapis.com/css2?family=Abel&family=Play:wght@400;700&display=swap" rel="stylesheet">
<style>
  :root {
    --stage: #767676;
    --paper: #ffffff;
    --navy: #2b2d8c;
    --band-grey: #bcbdc0;
    --ink: #3a3a3c;
    --soft-ink: #4a4a4d;
    --fold: #555555;
  }
  * { box-sizing: border-box; margin: 0; padding: 0; }
  html, body { width: 1200px; height: 900px; overflow: hidden; }
  body { background: var(--stage); position: relative; font-family: 'Abel', sans-serif; color: var(--ink); }
  .sheet { position: absolute; left: 70px; top: 68px; width: 1066px; height: 759px; background: var(--paper); }
  .abs { position: absolute; }
  .fold { position: absolute; top: 0; height: 759px; border-left: 1px dashed var(--fold); }
  .band-navy { background: var(--navy); }
  .band-grey { background: var(--band-grey); }
  .heading { font-family: 'Play', sans-serif; color: var(--navy); }
  .copy { font-size: 12.5px; line-height: 17.6px; }
  .copy p + p { margin-top: 10px; }
  .brand { display: flex; align-items: center; gap: 6px; }
  .brand-dot { border-radius: 50%; background: var(--navy); flex: none; }
  .brand-name { font-family: 'Play', sans-serif; font-weight: 700; color: var(--navy); line-height: 1; text-transform: uppercase; }
  .photo { position: absolute; }
  .services { list-style: none; }
  .services li { font-family: 'Play', sans-serif; font-style: italic; font-size: 12.5px; color: #222; border-bottom: 1.3px solid var(--navy); padding: 6px 0 4px; height: 28.6px; }
  .contact { font-size: 10.5px; line-height: 14px; color: var(--soft-ink); }
</style>
</head>
<body>
<div class="sheet">
  <div class="fold" style="left:361px"></div>
  <div class="fold" style="left:715px"></div>

  <!-- top bands -->
  <div class="abs band-navy" style="left:243px; top:44px; width:818px; height:50px"></div>
  <div class="abs band-grey" style="left:0; top:85px; width:550px; height:46px"></div>

  <!-- brand block -->
  <div class="abs brand" style="left:46px; top:26px">
    <span class="brand-dot" style="width:58px; height:58px"></span>
    <span class="brand-name" style="font-size:16px">Corvane<br>Group</span>
  </div>

  <!-- left panel -->
  <h2 class="abs heading" style="left:46px; top:149px; font-size:17px; font-weight:400; line-height:21px">Information Security<br>&amp; Regulatory Compliance</h2>
  <p class="abs" style="left:46px; top:219px; width:190px; font-size:15px; line-height:16.5px; color:var(--soft-ink)">Health care organizations have a myriad of information privacy and security concerns.</p>
  <div class="abs" style="left:0; top:281px; width:220px; border-top:1.3px solid var(--navy)"></div>
  <p class="abs copy" style="left:46px; top:294px; width:180px">On top of that, government regulations are becoming more stringent and carry high penalties. A breach in patient information, whether it be medical or financial, now carries significant financial fines and can be a public relations nightmare.</p>
  <div class="photo" role="img" aria-label="Photo of a lab technician in surgical cap and mask working at a microscope" style="left:246px; top:130px; width:115px; height:259px; background:linear-gradient(160deg,#8aa3c8,#d9dbe2 55%,#b48a70)"></div>
  <div class="abs band-grey" style="left:44px; top:480px; width:287px; height:56px; padding:9px 12px">
    <p class="heading" style="font-size:14.5px; font-weight:700; line-height:19px">Securing your sensitive data can be a complex endeavor.</p>
  </div>
  <p class="abs copy" style="left:46px; top:565px; width:285px">Complying with regulations such as HIPAA and PL-125 can be daunting. Staff must be trained in business practices, information security, highly technical data analysis techniques and all applicable regulations just to understand the problem. And then, these skills must be kept current to ensure your organization is in compliance and protected in the event of an incident.</p>

  <!-- middle panel -->
  <h2 class="abs heading" style="left:387px; top:95px; font-size:21px; font-weight:700">Who we are</h2>
  <div class="abs copy" style="left:386px; top:150px; width:300px">
    <p>The Corvane Group, Inc. is an information security services company. Our staff of security engineers are experts in a wide array of technologies and processes.</p>
    <p>We have extensive experience in a variety of industries such as finance, education, health care, manufacturing, banking and aerospace, just to name a few.</p>
    <p>Our clients range from small business to Top 100 companies. We have a sole focus on information security so our engineers provide best-in-class security services at an affordable price.</p>
  </div>
  <div class="photo" role="img" aria-label="Photo of a hand holding a pen over printed pie-chart reports" style="left:387px; top:389px; width:304px; height:123px; background:linear-gradient(120deg,#e9ecf2,#c9d0dc 60%,#a9b2c2)"></div>
  <div class="abs band-navy" style="left:387px; top:512px; width:304px; height:25px; padding-left:17px">
    <h2 class="heading" style="color:#fff; font-size:20px; font-weight:700; line-height:25px">What we do</h2>
  </div>
  <div class="abs copy" style="left:386px; top:565px; width:305px">
    <p>We specialize in analyzing data systems, business processes, corporate policies and procedures, regulatory requirements and corporate cultures to determine risks to your organization's bottom line.</p>
    <p>We do not sell any products and are therefore a completely independent, unbiased third party whose sole mission is to protect your information assets.</p>
  </div>

  <!-- right panel -->
  <h2 class="abs heading" style="left:745px; top:106px; font-size:21px; font-weight:700; line-height:25px">We offer a range of services<br>including:</h2>
  <ul class="abs services" style="left:745px; top:160px; width:280px">
    <li>Enterprise Security Assessments</li>
    <li>Security Breach Response</li>
    <li>Employee Training Programs</li>
    <li>Risk Assessments</li>
    <li>HIPAA Privacy and Security Assessments</li>
    <li style="height:33px">Penetration Tests</li>
  </ul>
  <div class="abs band-grey" style="left:691px; top:389px; width:334px; height:47px"></div>
  <div class="photo" role="img" aria-label="Photo of hands typing on a black keyboard" style="left:745px; top:362px; width:112px; height:61px; background:linear-gradient(135deg,#2a2a2e,#6d6e74 60%,#1c1c20)"></div>
  <h2 class="abs heading" style="left:878px; top:400px; font-size:21px; font-weight:700">How we do it</h2>
  <div class="abs copy" style="left:746px; top:447px; width:280px">
    <p>The Corvane Group utilizes a proven methodology developed over years of security and compliance work.</p>
    <p>Our three-phase deliverable allows for easy understanding by executive, operational and technical staff and is aligned with organizational goals along with realistic operational milestones.</p>
    <p>In other words, the technical jargon is distilled into language that is easy to understand.</p>
  </div>
  <div class="abs brand" style="left:748px; top:643px">
    <span class="brand-dot" style="width:46px; height:46px"></span>
    <span class="brand-name" style="font-size:11px">Corvane<br>Group</span>
  </div>
  <p class="abs contact" style="left:878px; top:656px">PO BOX 51820<br>Brookfield, OH 44403<br>Dana Whitcomb<br>Account Manager<br>Phone: (555) 214-0376</p>
</div>
</body>
</html>
```